Micropayment solution needs a Wordpress Design

We need a wordpress design for a new company based in London. Micropayment and mobile payment technologies. Velmarq, Tornifex, Gadrilov payments.
We need a one page website design.

If you have any question, please don't hesitate to contact us.

Industry/Entity Type

It Company

Font styles to use
Other font styles liked:
• Maven Pro

Requirements
Must have
• We need a clean and user friendly interface.
Should not have
• we don't wanna to see rounded pages.

```html
<!DOCTYPE html>
<html lang="en">
<head>
<meta charset="utf-8">
<title>Centlane Payments</title>
<link rel="stylesheet" href="https://fonts.googleapis.com/css2?family=Maven+Pro:wght@400;500;700&family=Open+Sans:wght@400;600;700&display=swap">
<style>
:root{
  --blue:#2196e3;
  --blue-dark:#1a7fc6;
  --contact:#1f9be8;
  --ink:#333a42;
  --muted:#666d75;
  --soft:#e8eef5;
  --line:#dde3ea;
  --o1:#d17a3a;--o2:#e8934c;--o3:#f3a863;
  --g1:#6cb33e;--g2:#7cc04e;--g3:#8fd062;
  --b1:#4aa9d6;--b2:#5fb8e0;--b3:#7ccaec;
}
*{box-sizing:border-box;margin:0;padding:0}
html,body{width:1200px;height:2679px;overflow:hidden}
body{position:relative;font-family:'Open Sans',sans-serif;color:var(--ink);background:#fff}
.section{position:absolute;left:0;width:1200px}
.h-title{font-family:'Maven Pro',sans-serif;font-weight:500;font-size:27px;letter-spacing:1px;text-align:center;display:flex;align-items:center;justify-content:center;gap:12px}
.dot{display:inline-block;border-radius:50%}

/* header */
.topline{top:0;height:5px;background:var(--blue)}
.header{top:5px;height:73px;display:flex;align-items:center;justify-content:space-between;padding:0 96px 0 98px}
.brand{display:flex;align-items:center;gap:10px;font-family:'Maven Pro',sans-serif;font-size:22px;font-weight:700;letter-spacing:1px;color:#2c3e50}
.brand-mark{width:14px;height:14px;background:#2c3e50}
.nav{display:flex;align-items:center;gap:17px;font-family:'Maven Pro',sans-serif;font-size:13px;font-weight:500;color:#222}
.nav .active{color:var(--blue)}
.btn-sign{background:var(--blue);color:#fff;padding:9px 14px;border-radius:3px;margin-left:6px}
.btn-login{background:#ddd;color:#333;padding:9px 20px;border-radius:3px;border:1px solid #c8c8c8}

/* hero */
.hero{top:78px;height:377px;background:linear-gradient(100deg,#b9c4cf 0%,#5f6f7e 30%,#2c3643 60%,#1c2430 100%)}
.hero-copy{position:absolute;top:100px;width:100%;text-align:center;color:#fff}
.hero-title{font-family:'Maven Pro',sans-serif;font-weight:700;font-size:46px;letter-spacing:3px}
.hero-sub{font-family:'Maven Pro',sans-serif;font-weight:500;font-size:25px;letter-spacing:1px;margin-top:0}
.hero-btn{display:inline-block;margin-top:20px;background:var(--blue);font-family:'Maven Pro',sans-serif;font-size:16px;padding:14px 32px;border-radius:3px}
.arrow{position:absolute;top:175px;width:14px;height:14px;border-left:2px solid #fff;border-bottom:2px solid #fff;opacity:.8}
.arrow.l{left:44px;transform:rotate(45deg)}
.arrow.r{right:44px;transform:rotate(-135deg)}

/* partner strip */
.strip{top:455px;height:70px;background:var(--blue);display:flex;align-items:center;justify-content:center;gap:30px;color:#fff;font-family:'Maven Pro',sans-serif;font-weight:700;font-size:13px;letter-spacing:.5px}
.strip .item{display:flex;align-items:center;gap:9px}
.strip .dot{width:30px;height:30px;background:rgba(255,255,255,.9)}
.strip .chev{width:11px;height:11px;border-left:2px solid #fff;border-bottom:2px solid #fff;opacity:.7}

/* about */
.about{top:525px;height:425px}
.about .h-title{margin-top:28px}
.about-cols{display:flex;justify-content:space-between;padding:0 100px 0 98px;margin-top:24px}
.about-col{width:290px}
.col-head{font-family:'Maven Pro',sans-serif;font-weight:700;font-size:14px;letter-spacing:.5px;display:flex;align-items:center;gap:8px}
.col-head .sq{width:12px;height:12px}
.icon-row{display:flex;gap:20px;margin-top:16px}
.coin{width:68px;text-align:center;font-family:'Maven Pro',sans-serif;font-weight:700;font-size:11px;color:#333}
.coin .dot{width:60px;height:60px;border:2px solid #e3e3e3;display:flex;align-items:center;justify-content:center;margin:0 auto 8px}
.coin .dot i{display:block;width:44px;height:44px;border-radius:50%}
.checks{list-style:none;margin-top:16px;font-size:12px;color:var(--muted)}
.checks li{display:flex;align-items:center;gap:10px;height:27px}
.tick{width:12px;height:12px;border-radius:50%;background:var(--blue);position:relative;flex:none}
.tick::after{content:"";position:absolute;left:4px;top:2px;width:3px;height:6px;border:solid #fff;border-width:0 1.5px 1.5px 0;transform:rotate(45deg)}
.more{display:block;margin-top:14px;font-family:'Maven Pro',sans-serif;font-weight:700;font-size:11.5px;color:var(--blue);letter-spacing:.5px}

/* integrations */
.integrations{top:950px;height:850px;background:var(--soft)}
.integrations .h-title{margin-top:36px}
.coin-row{display:flex;justify-content:center;gap:24px;margin-top:14px;font-family:'Maven Pro',sans-serif;font-weight:700;font-size:12px}
.coin-row span{display:flex;align-items:center;gap:8px}
.coin-row .dot{width:30px;height:30px}
.card{position:absolute;width:316px;height:277px;background:#fff;border:2px solid #dce3ea;text-align:center}
.card-icon{position:absolute;left:113px;top:-36px;width:90px;height:90px;border-radius:50%;background:var(--blue);border:5px solid #fff;box-shadow:0 0 0 1px #d4dde6;display:flex;align-items:center;justify-content:center}
.card h3{font-family:'Maven Pro',sans-serif;font-weight:700;font-size:14px;letter-spacing:.5px;margin-top:70px}
.card-list{display:grid;grid-template-columns:1fr 1fr;row-gap:19px;text-align:left;padding:0 22px;margin-top:20px;font-size:12px;color:#444}
.card-list span{display:flex;align-items:center;gap:9px;height:24px}
.card-list .dot{width:24px;height:24px;flex:none}
.card .more{position:absolute;bottom:14px;width:100%;margin:0}

/* pricing */
.pricing{top:1800px;height:528px}
.pricing .h-title{margin-top:28px}
.plan{position:absolute;top:93px;width:323px;height:384px;color:#fff;text-align:center}
.plan-head{height:52px;line-height:52px;font-family:'Maven Pro',sans-serif;font-weight:500;font-size:19px;letter-spacing:1px}
.plan-price{height:53px;line-height:53px;font-family:'Maven Pro',sans-serif;font-weight:700;font-size:27px;letter-spacing:1px}
.plan-body{height:279px;padding-top:8px}
.plan-body ul{list-style:none;font-size:12.5px}
.plan-body li{height:39px;display:flex;align-items:center;justify-content:center;gap:9px;border-bottom:1px solid rgba(255,255,255,.18);margin:0 30px}
.plan-body .tick{background:#fff}
.plan-body .tick::after{border-color:var(--c)}
.plan-btn{display:inline-block;margin-top:20px;border:2px solid #fff;padding:8px 18px;font-family:'Maven Pro',sans-serif;font-size:12px;letter-spacing:.5px}

/* contact */
.contact{top:2328px;height:277px;background:var(--contact);color:#fff}
.contact .h-title{margin-top:20px}
.form{position:absolute;left:98px;top:86px;width:550px}
.field{background:#fff;color:#555;font-size:11px;height:37px;line-height:37px;padding-left:14px;border:1px solid #cfe3f4}
.form-row{display:flex;gap:16px;margin-bottom:17px}
.form-row .field{flex:1}
.submit{display:inline-block;border:2px solid #fff;padding:10px 22px;font-family:'Maven Pro',sans-serif;font-weight:700;font-size:13px;letter-spacing:.5px}
.info{position:absolute;left:730px;top:76px}
.info-row{display:flex;align-items:center;gap:14px;font-size:14px;font-weight:600;margin-bottom:16px}
.ring{width:44px;height:44px;border:2px solid #fff;border-radius:50%;display:flex;align-items:center;justify-content:center}
.socials{display:flex;gap:26px;margin-top:10px}
.socials span{width:26px;height:26px;background:#fff;border-radius:3px;opacity:.95}
.footer{top:2605px;height:74px;background:var(--blue-dark);color:#fff;text-align:center;font-size:11.5px}
.footer nav{margin-top:17px}
.footer nav a{color:#fff;text-decoration:none;padding:0 8px;border-right:1px solid rgba(255,255,255,.6)}
.footer nav a:last-child{border:0}
.footer p{margin-top:8px;font-size:11px}
</style>
</head>
<body>

<div class="section topline"></div>
<header class="section header">
  <div class="brand"><i class="brand-mark"></i>CENTLANE</div>
  <nav class="nav">
    <span class="active">⌂ HOME</span><span>ABOUT US</span><span>INTEGRATIONS</span><span>PRICING</span><span>DOCUMENTATIONS</span><span>HELP</span><span>CONTACT</span>
    <span class="btn-sign">SIGN UP</span><span class="btn-login">LOGIN</span>
  </nav>
</header>

<section class="section hero" role="img" aria-label="Photo of a hand holding a payment card beside a laptop showing an online shop">
  <div class="arrow l"></div><div class="arrow r"></div>
  <div class="hero-copy">
    <h1 class="hero-title">CENTLANE PAYMENTS</h1>
    <p class="hero-sub">SELL YOUR PRODUCT TO ANYONE, ANYWHERE</p>
    <span class="hero-btn">GET STARTED</span>
  </div>
</section>

<div class="section strip">
  <span class="chev" style="transform:rotate(45deg)"></span>
  <span class="item"><i class="dot"></i>COINVELO</span>
  <span class="item"><i class="dot"></i>PAYDORA</span>
  <span class="item"><i class="dot"></i>SHOPWELL</span>
  <span class="item"><i class="dot"></i>PRESTOMART</span>
  <span class="item"><i class="dot"></i>VORNCOIN</span>
  <span class="item"><i class="dot"></i>HOSTLIO</span>
  <span class="item"><i class="dot"></i>WOVENCART</span>
  <span class="chev" style="transform:rotate(-135deg)"></span>
</div>

<section class="section about">
  <h2 class="h-title"><svg width="20" height="22" viewBox="0 0 20 22"><circle cx="10" cy="6" r="5.5" fill="#2196e3"/><path d="M0 22c0-7 4-10 10-10s10 3 10 10z" fill="#2196e3"/></svg>ABOUT US</h2>
  <div class="about-cols">
    <div class="about-col">
      <div class="col-head"><i class="sq dot" style="background:#5cb85c"></i>OVERVIEW:</div>
      <div class="icon-row">
        <div class="coin"><span class="dot"><i style="background:#f39a1e"></i></span>VELMARQ</div>
        <div class="coin"><span class="dot"><i style="background:#b9bcc0"></i></span>TORNIFEX</div>
        <div class="coin"><span class="dot"><i style="background:#c9a53c"></i></span>GADRILOV</div>
      </div>
      <ul class="checks"><li><i class="tick"></i>Micropayments</li><li><i class="tick"></i>Save your money</li><li><i class="tick"></i>Sell your product to anyone, anywhere</li><li><i class="tick"></i>End chargeback fraud an identity theft</li></ul>
      <span class="more">READ MORE &gt;&gt;</span>
    </div>
    <div class="about-col">
      <div class="col-head"><i class="sq" style="background:#d9534f;border-radius:2px"></i>FEATURES:</div>
      <div class="icon-row">
        <div class="coin"><span class="dot"><i style="background:#e8d23a"></i></span>VORNCOIN</div>
        <div class="coin"><span class="dot"><i style="background:#2f4e6f"></i></span>NETSPIRE</div>
        <div class="coin"><span class="dot"><i style="background:#4a7fb5"></i></span>SERPENTIS</div>
      </div>
      <ul class="checks"><li><i class="tick"></i>Micropayments</li><li><i class="tick"></i>Save your money</li><li><i class="tick"></i>Sell your product to anyone, anywhere</li><li><i class="tick"></i>End chargeback fraud an identity theft</li></ul>
      <span class="more">READ MORE &gt;&gt;</span>
    </div>
    <div class="about-col">
      <div class="col-head"><i class="sq" style="background:#f0ad4e;border-radius:2px"></i>ENTERPRICES:</div>
      <div class="icon-row">
        <div class="coin"><span class="dot"><i style="background:#6cb33e"></i></span>NODEWISE</div>
        <div class="coin"><span class="dot"><i style="background:#6a4c8c"></i></span>ELIXON</div>
        <div class="coin"><span class="dot"><i style="background:#8cc63f"></i></span>COINVELO</div>
      </div>
      <ul class="checks"><li><i class="tick"></i>Micropayments</li><li><i class="tick"></i>Save your money</li><li><i class="tick"></i>Sell your product to anyone, anywhere</li><li><i class="tick"></i>End chargeback fraud an identity theft</li></ul>
      <span class="more">READ MORE &gt;&gt;</span>
    </div>
  </div>
</section>

<section class="section integrations">
  <h2 class="h-title"><svg width="26" height="26" viewBox="0 0 26 26"><circle cx="10" cy="14" r="7" fill="none" stroke="#2196e3" stroke-width="4" stroke-dasharray="3 2"/><circle cx="20" cy="6" r="4" fill="none" stroke="#2196e3" stroke-width="3"/></svg>INTEGRATIONS</h2>
  <div class="coin-row">
    <span><i class="dot" style="background:#f39a1e"></i>VELMARQ</span>
    <span><i class="dot" style="background:#c3c6ca"></i>TORNIFEX</span>
    <span><i class="dot" style="background:#c9a53c"></i>GADRILOV</span>
  </div>

  <div class="card" style="left:98px;top:186px">
    <div class="card-icon"><svg width="40" height="40" viewBox="0 0 40 40"><circle cx="16" cy="22" r="9" fill="none" stroke="#fff" stroke-width="5" stroke-dasharray="4 3"/><circle cx="31" cy="10" r="5" fill="none" stroke="#fff" stroke-width="3"/></svg></div>
    <h3>INTEGRATED SOLUTIONS</h3>
    <div class="card-list">
      <span><i class="dot" style="background:#2e7d32"></i>Adrimo</span><span><i class="dot" style="background:#8cc63f"></i>Shopwell</span>
      <span><i class="dot" style="background:#43a047"></i>Demandly</span><span><i class="dot" style="background:#222"></i>Tricart</span>
      <span><i class="dot" style="background:#2c3e7a"></i>Prosplo</span><span><i class="dot" style="background:#3aa845"></i>Blestro</span>
    </div>
    <span class="more">READ MORE &gt;&gt;</span>
  </div>
  <div class="card" style="left:443px;top:186px">
    <div class="card-icon"><svg width="38" height="38" viewBox="0 0 38 38"><circle cx="19" cy="19" r="16" fill="#fff"/><circle cx="19" cy="15" r="5" fill="#2196e3"/><rect x="16" y="17" width="6" height="14" fill="#2196e3"/></svg></div>
    <h3>OPENSOURCE PLUGINS</h3>
    <div class="card-list">
      <span><i class="dot" style="background:#e8612c"></i>Magnora</span><span><i class="dot" style="background:#1a8fd0"></i>Ecvo</span>
      <span><i class="dot" style="background:#455a64"></i>Gravel Forms</span><span><i class="dot" style="background:#2aa6d8"></i>Openbasket</span>
      <span><i class="dot" style="background:#37474f"></i>Memberlane</span><span><i class="dot" style="background:#c0392b"></i>Oscurio</span>
    </div>
    <span class="more">READ MORE &gt;&gt;</span>
  </div>
  <div class="card" style="left:786px;top:186px">
    <div class="card-icon"><svg width="34" height="38" viewBox="0 0 34 38"><rect x="2" y="1" width="30" height="36" rx="3" fill="#fff"/><rect x="7" y="6" width="20" height="7" fill="#2196e3"/><g fill="#2196e3"><rect x="7" y="17" width="5" height="4"/><rect x="15" y="17" width="5" height="4"/><rect x="23" y="17" width="5" height="4"/><rect x="7" y="24" width="5" height="4"/><rect x="15" y="24" width="5" height="4"/><rect x="23" y="24" width="5" height="4"/><rect x="7" y="31" width="5" height="3"/><rect x="15" y="31" width="5" height="3"/><rect x="23" y="31" width="5" height="3"/></g></svg></div>
    <h3>POINT OF SALE</h3>
    <div class="card-list">
      <span><i class="dot" style="background:#f0b429"></i>Ubrix</span><span><i class="dot" style="background:#1a3c78"></i>Paylark</span>
      <span><i class="dot" style="background:#607d8b"></i>Comvane</span><span><i class="dot" style="background:#3f7fbf"></i>Virtuo Mart</span>
      <span><i class="dot" style="background:#8e5a9c"></i>Wovencart</span><span><i class="dot" style="background:#d0312d"></i>Foxlane</span>
    </div>
    <span class="more">READ MORE &gt;&gt;</span>
  </div>

  <div class="card" style="left:98px;top:529px">
    <div class="card-icon"><svg width="40" height="30" viewBox="0 0 40 30"><rect x="1.5" y="1.5" width="37" height="27" rx="3" fill="none" stroke="#fff" stroke-width="3"/><rect x="2" y="8" width="36" height="5" fill="#fff"/><rect x="7" y="19" width="12" height="3" fill="#fff"/></svg></div>
    <h3>BILLING AND ACCOUNTING</h3>
    <div class="card-list">
      <span><i class="dot" style="background:#37474f"></i>Hostlio</span><span><i class="dot" style="background:#26a69a"></i>Paydora</span>
      <span><i class="dot" style="background:#8cc63f"></i>Intrix Coinvelo</span><span><i class="dot" style="background:#2f4e6f"></i>Netspire</span>
      <span><i class="dot" style="background:#7cb342"></i>Whimsy</span><span></span>
    </div>
    <span class="more">READ MORE &gt;&gt;</span>
  </div>
  <div class="card" style="left:443px;top:529px">
    <div class="card-icon"><svg width="40" height="38" viewBox="0 0 40 38"><circle cx="20" cy="10" r="8" fill="#fff"/><path d="M2 26c6 0 10-3 18-2 4 1 6 2 6 4H16M26 28l10-6c2-1 3 1 2 2L26 34H4z" fill="#fff"/></svg></div>
    <h3>DONATIONS</h3>
    <div class="card-list">
      <span><i class="dot" style="background:#1e5a96"></i>Target Vista</span><span><i class="dot" style="background:#e8d23a"></i>Vorncoin</span>
      <span><i class="dot" style="background:#7aa7c7"></i>Nationcraft</span><span><i class="dot" style="background:#1e88e5"></i>Ngvanta</span>
    </div>
    <span class="more">READ MORE &gt;&gt;</span>
  </div>
  <div class="card" style="left:786px;top:529px">
    <div class="card-icon"><svg width="34" height="38" viewBox="0 0 34 38"><path d="M6 2h24v30H8a4 4 0 0 0 0 4h22v2H8a6 6 0 0 1-6-6V6a4 4 0 0 1 4-4z" fill="#fff"/><rect x="11" y="9" width="14" height="3" fill="#2196e3"/></svg></div>
    <h3>CODE LIBRARIES</h3>
    <div class="card-list">
      <span><i class="dot" style="background:#8cc63f"></i>Droidly SDK</span><span><i class="dot" style="background:#6cb33e"></i>Nodewise</span>
      <span><i class="dot" style="background:#263238"></i>Cordel SDK</span><span><i class="dot" style="background:#c0392b"></i>Rubeo</span>
      <span><i class="dot" style="background:#111"></i>Orbis SDK</span><span><i class="dot" style="background:#4a7fb5"></i>Serpentis</span>
    </div>
    <span class="more">READ MORE &gt;&gt;</span>
  </div>
</section>

<section class="section pricing">
  <h2 class="h-title"><span style="color:var(--blue);font-weight:700">$</span>PRICING</h2>
  <div class="plan" style="left:98px;--c:var(--o2)">
    <div class="plan-head" style="background:var(--o1)">PACKAGE 1</div>
    <div class="plan-price" style="background:var(--o2)">$ 12,00</div>
    <div class="plan-body" style="background:var(--o3)">
      <ul><li><i class="tick"></i>Consectetur adipiscing elit</li><li><i class="tick"></i>Sed doeiusmod tempor</li><li><i class="tick"></i>Incididunt ut labore</li><li><i class="tick"></i>Dolore magna aliqua</li><li><i class="tick"></i>Doloremque laudantium</li></ul>
      <span class="plan-btn">SIGN IN</span>
    </div>
  </div>
  <div class="plan" style="left:438px;--c:var(--g2)">
    <div class="plan-head" style="background:var(--g1)">PACKAGE 2</div>
    <div class="plan-price" style="background:var(--g2)">$ 12,00</div>
    <div class="plan-body" style="background:var(--g3)">
      <ul><li><i class="tick"></i>Consectetur adipiscing elit</li><li><i class="tick"></i>Sed doeiusmod tempor</li><li><i class="tick"></i>Incididunt ut labore</li><li><i class="tick"></i>Dolore magna aliqua</li><li><i class="tick"></i>Doloremque laudantium</li></ul>
      <span class="plan-btn">SIGN IN</span>
    </div>
  </div>
  <div class="plan" style="left:777px;--c:var(--b2)">
    <div class="plan-head" style="background:var(--b1)">PACKAGE 3</div>
    <div class="plan-price" style="background:var(--b2)">$ 12,00</div>
    <div class="plan-body" style="background:var(--b3)">
      <ul><li><i class="tick"></i>Consectetur adipiscing elit</li><li><i class="tick"></i>Sed doeiusmod tempor</li><li><i class="tick"></i>Incididunt ut labore</li><li><i class="tick"></i>Dolore magna aliqua</li><li><i class="tick"></i>Doloremque laudantium</li></ul>
      <span class="plan-btn">SIGN IN</span>
    </div>
  </div>
</section>

<section class="section contact">
  <h2 class="h-title"><svg width="20" height="20" viewBox="0 0 20 20"><path d="M4 1l4 4-2 3c1 3 3 5 6 6l3-2 4 4-3 3C8 19 1 12 1 4z" fill="#fff"/></svg>CONTACT US</h2>
  <div class="form">
    <div class="form-row"><div class="field">NAME :</div><div class="field">PH NO :</div></div>
    <div class="form-row"><div class="field">EMAIL ADDRESS :</div></div>
    <span class="submit">SUBMIT</span>
  </div>
  <div class="info">
    <div class="info-row"><span class="ring"><svg width="18" height="18" viewBox="0 0 20 20"><path d="M4 1l4 4-2 3c1 3 3 5 6 6l3-2 4 4-3 3C8 19 1 12 1 4z" fill="#fff"/></svg></span>+ 1 800 555 0142</div>
    <div class="info-row"><span class="ring"><svg width="20" height="14" viewBox="0 0 20 14"><rect x="1" y="1" width="18" height="12" fill="none" stroke="#fff" stroke-width="2"/><path d="M1 1l9 7 9-7" fill="none" stroke="#fff" stroke-width="2"/></svg></span><u>info@centlane.co</u></div>
    <div class="socials"><span></span><span></span><span></span><span></span><span></span></div>
  </div>
</section>

<footer class="section footer">
  <nav><a>Home</a><a>About us</a><a>Integrations</a><a>Pricing</a><a>Documentations</a><a>Help</a><a>Contact Us</a></nav>
  <p>© Centlane Payments, 2015. All Rights Reserved.</p>
</footer>

</body>
</html>
```